Criminal Defense Law Firm needs Stationary design Theme for a Business Card, Envelope, and Letterhea

Our Law Firm is seeking a general design concept for a business card, letterhead, and Envelope.

Our website is WillowcrestTrialDesk.com

A design for these three items is requested to keep branding in place for the firm. Would like to keep the Firm Colors on the website consistent with our branding on business cards, letterheads, and mailing envelopes #10 size to be exact.

We would like business cards printed front and back with Law firm Colors from website.

Letterhead with law firm colors as well. Design is not limited to just the header, but the footer can be utilized as well for email, website, phone, fax, etc.

Simple #10 envelope consisting of the same design principles set out in the previous two designs.

```html
<!DOCTYPE html>
<html lang="en">
<head>
<meta charset="utf-8">
<title>Willowcrest Trial Law Offices — Stationery</title>
<link href="https://fonts.googleapis.com/css2?family=Crimson+Pro:wght@400&family=Questrial&display=swap" rel="stylesheet">
<style>
  :root {
    --backdrop: #8b8b8b;
    --paper: #f4f4f4;
    --paper-shade: #ebebeb;
    --gold: #a58c5a;
    --gold-text: #b08f4c;
    --ink: #3a3a3a;
    --ink-soft: #5c5c5c;
    --edge: #3b3b3b;
    --liner: #ece7da;
    --mark-faint: #e2e2e2;
  }
  * { box-sizing: border-box; margin: 0; padding: 0; }
  html, body { width: 1200px; height: 800px; overflow: hidden; }
  body { background: var(--backdrop); position: relative; font-family: "Questrial", sans-serif; }

  .envelope-back, .envelope-front, .letterhead { position: absolute; }

  /* envelope back, flap open */
  .envelope-back { left: 72px; top: 64px; width: 472px; height: 338px; }
  .envelope-back svg { display: block; }

  /* envelope front */
  .envelope-front { left: 86px; top: 422px; width: 460px; height: 306px; background: var(--paper); overflow: hidden; }
  .envelope-front .flap-band { position: absolute; left: 0; top: 0; width: 100%; height: 76px; background: var(--gold); }
  .envelope-front .flap-seal { position: absolute; left: 212px; top: 32px; width: 18px; height: 18px; border: 1.2px solid #f3ecdc; border-radius: 50%; }
  .envelope-front .bottom-edge { position: absolute; left: 0; bottom: 0; width: 100%; height: 10px; background: var(--edge); }

  .letterhead { left: 630px; top: 88px; width: 425px; height: 648px; background: linear-gradient(180deg, var(--paper) 0%, var(--paper-shade) 30%, var(--paper) 31%, var(--paper-shade) 62%, var(--paper) 63%, var(--paper) 100%); overflow: hidden; }
  .letterhead .top-rule { position: absolute; left: 0; top: 0; width: 100%; height: 6px; background: var(--gold); }
  .letterhead .bottom-edge { position: absolute; left: 0; bottom: 0; width: 100%; height: 10px; background: var(--edge); }

  .firm-id { position: absolute; display: flex; align-items: center; gap: 9px; }
  .firm-id .dot { width: 25px; height: 25px; border: 1.3px solid var(--ink); border-radius: 50%; flex: none; }
  .firm-name { font-family: "Crimson Pro", serif; font-weight: 400; font-size: 13px; line-height: 13px; letter-spacing: 0.6px; color: var(--ink); text-transform: uppercase; }

  .envelope-front .firm-id { left: 34px; top: 116px; }
  .letterhead .firm-id { left: 96px; top: 46px; }

  .faint-circle { position: absolute; border: 4px solid var(--mark-faint); border-radius: 50%; }
  .envelope-front .faint-circle { left: 282px; top: 112px; width: 148px; height: 148px; }
  .letterhead .faint-circle { left: 98px; top: 180px; width: 278px; height: 278px; }

  .footer-line { position: absolute; display: flex; justify-content: space-between; align-items: baseline; font-size: 6.5px; color: var(--ink-soft); }
  .footer-line .label { color: var(--gold-text); }
  .footer-line .web { letter-spacing: 1.4px; color: var(--gold-text); }
  .envelope-front .footer-line { left: 40px; right: 36px; bottom: 26px; }
  .letterhead .footer-line { left: 33px; right: 36px; bottom: 40px; }
</style>
</head>
<body>

  <div class="envelope-back">
    <svg width="472" height="338" viewBox="0 0 472 338">
      <path d="M0 14 Q0 0 14 0 H458 Q472 0 472 14 V338 H0 Z" fill="#eeeeee"/>
      <rect role="img" aria-label="Envelope liner with a repeating firm pattern in cream tones" x="0" y="0" width="472" height="130" rx="12" fill="var(--liner)"/>
      <path d="M0 110 L40 130 H432 L472 110 V338 H0 Z" fill="#f2f2f2"/>
      <path d="M0 110 L40 130 H432 L472 110" fill="none" stroke="#e0e0e0" stroke-width="1"/>
    </svg>
  </div>

  <div class="envelope-front">
    <div class="flap-band"></div>
    <div class="flap-seal"></div>
    <div class="faint-circle"></div>
    <div class="firm-id">
      <span class="dot"></span>
      <span class="firm-name">Willowcrest Trial<br>Law Offices</span>
    </div>
    <div class="footer-line">
      <span>1450 Alder Lane NW, Cedar Ridge, NM 87000 · <span class="label">Phone:</span> 555.014.2290</span>
      <span class="web">www.willowcresttrialdesk.com</span>
    </div>
    <div class="bottom-edge"></div>
  </div>

  <div class="letterhead">
    <div class="top-rule"></div>
    <div class="faint-circle"></div>
    <div class="firm-id">
      <span class="dot"></span>
      <span class="firm-name">Willowcrest Trial<br>Law Offices</span>
    </div>
    <div class="footer-line">
      <span>1450 Alder Lane NW, Cedar Ridge, NM 87000 · <span class="label">Phone:</span> 555.014.2290</span>
      <span class="web">www.willowcresttrialdesk.com</span>
    </div>
    <div class="bottom-edge"></div>
  </div>

</body>
</html>
```